Brochure Design Project

We need a brochure for our acting school, website is
www.thestagelanternhall.com - It needs to reflect youth, vitality, and people's DREAMS coming true...colors should be red and black, but open to something new as well...the courses included should be
Players' Spark Week, Rising Talent Bundle, And The Masterclass Track

Emphasis on Players' Spark Week is the short term intensity.
Rising Talent Bundle is the benefit of getting all the tools to look for acting work.
Masterclass Track is becoming a pro, and if you are in another country, being provided with a visa to come to the U.S.

I have attached pictures and logos...I will submit the copy once there is a framework...the OLD brochure is attached as well...

Thank you...

Harold

Project Deadline Extended
Reason: We would like to see a couple more ideas...

Project Deadline Extended
Reason: HI there designers! Thanks for your submissions. We are almost ready to pick a design. Thanks for the understanding.

Target Market(s)

18-35 year olds...fairly affluent, educated, American, European, or Australian

Industry/Entity Type

School

Requirements
Must have
• Make it fun, clean, clear, and NOT corporate.

```html
<!DOCTYPE html>
<html lang="en">
<head>
<meta charset="utf-8">
<title>Players' Spark Week Brochure</title>
<link href="https://fonts.googleapis.com/css2?family=Oswald:wght@500;700&family=Open+Sans:wght@400;700&family=Boogaloo&display=swap" rel="stylesheet">
<style>
:root{
  --crimson:#8c1d20;
  --crimson-deep:#6d1316;
  --cream:#f6efdc;
  --gold:#e0a823;
  --ink:#2b2220;
  --white:#ffffff;
  --backdrop:#3b3b3d;
}
*{box-sizing:border-box;margin:0;padding:0}
html,body{width:1200px;height:986px;overflow:hidden;background:var(--backdrop)}
body{position:relative;font-family:'Open Sans',Arial,sans-serif}
.spread{position:absolute;left:290px;width:620px;height:479px;overflow:hidden;box-shadow:0 4px 14px rgba(0,0,0,.45)}
.spread--outside{top:10px;background:var(--crimson)}
.spread--inside{top:497px;background:var(--cream)}
.fold{position:absolute;top:0;bottom:0;width:1px;background:rgba(0,0,0,.12)}
.abs{position:absolute}
.photo{position:absolute;background:linear-gradient(135deg,#5a2a22,#c08a62 55%,#3a1f1a)}
.photo--round{border-radius:50%;border:3px solid var(--white)}
.tag{position:absolute;background:var(--white);color:var(--crimson);font:700 7px/1 'Oswald',sans-serif;text-transform:uppercase;padding:3px 4px;letter-spacing:.3px}
.head-duration{position:absolute;font:700 13px/1 'Oswald',sans-serif;color:var(--white)}
.copy{position:absolute;font-size:5.6px;line-height:1.45;color:var(--white)}
.copy--dark{color:var(--ink)}
.brand{position:absolute;display:flex;align-items:center;gap:5px;font:700 13px/1.05 'Oswald',sans-serif;color:var(--white);text-transform:uppercase}
.brand__dot{width:12px;height:12px;border-radius:50%;background:var(--white);flex:none}
.cover-title{position:absolute;left:432px;top:100px;width:180px;text-align:center;font:700 30px/1 'Oswald',sans-serif;color:var(--white);text-transform:uppercase}
.contact{position:absolute;left:232px;top:200px;width:150px;text-align:center;color:var(--white)}
.contact__addr{font-size:6.4px;line-height:1.45;margin-top:6px}
.contact__phone{font:700 17px/1 'Oswald',sans-serif;margin-top:5px}
.contact__web{font-size:6.2px;line-height:1.5;margin-top:3px}
.tagline{position:absolute;font-family:'Boogaloo',cursive;letter-spacing:1px}
.tagline--red{left:60px;top:420px;font-size:34px;color:var(--crimson)}
.tagline--white{left:220px;top:436px;font-size:28px;color:var(--white)}
.quote-name{position:absolute;font:700 6.5px/1 'Open Sans',sans-serif;color:var(--white)}
.gold-box{position:absolute;background:var(--gold);color:var(--white);padding:8px 10px;font:700 22px/1 'Oswald',sans-serif}
.gold-box span{display:block}
.gold-box .small{font-size:17px}
.section-head{position:absolute;font:700 8px/1.2 'Oswald',sans-serif;color:var(--crimson);text-transform:uppercase}
.section-head em{font-style:normal;display:block;font-size:7px;color:var(--ink)}
.sign-name{position:absolute;font-size:6px;line-height:1.4;color:var(--gold);font-weight:700}
.badge{position:absolute;display:flex;align-items:center;gap:4px;font:700 9px/1.05 'Oswald',sans-serif;color:var(--crimson);text-transform:uppercase}
.badge__sq{width:12px;height:12px;background:var(--crimson);flex:none}
svg.layer{position:absolute;left:0;top:0}
</style>
</head>
<body>

<section class="spread spread--outside" aria-label="Brochure outside">
  <svg class="layer" width="620" height="479" viewBox="0 0 620 479" aria-hidden="true">
    <path d="M0 330 C150 300 330 380 620 300 L620 479 L0 479 Z" fill="var(--cream)"/>
    <path d="M0 330 C150 300 330 380 620 300" fill="none" stroke="var(--gold)" stroke-width="3"/>
  </svg>
  <svg class="layer" width="620" height="479" viewBox="0 0 620 479" role="img" aria-label="Curved film strip decoration">
    <path d="M0 345 C150 315 330 395 560 318 L560 370 C330 450 150 370 0 400 Z" fill="var(--white)" opacity=".92"/>
  </svg>

  <div class="fold" style="left:206px"></div>
  <div class="fold" style="left:413px"></div>

  <span class="tag" style="left:12px;top:12px">The Advanced<br>Program</span>
  <div class="head-duration" style="left:74px;top:12px">Ongoing</div>
  <p class="copy" style="left:74px;top:28px;width:124px">Our continuing, committed actors train weekly to sharpen audition skills, build new scenes and keep the craft alive between bookings. Classes stay small so every player gets real notes and real stage time.</p>
  <p class="copy" style="left:12px;top:90px;width:186px">Working actors return here to stay ready. We pair cold reads, on-camera drills and scene study with honest coaching from teachers who still work in the industry every single week.</p>

  <span class="tag" style="left:12px;top:150px">The Masterclass<br>Track</span>
  <div class="head-duration" style="left:96px;top:150px">9 months</div>
  <p class="copy" style="left:12px;top:176px;width:186px">Designed for actors who plan a real career. Students from abroad may qualify for visa support to study in the U.S. You finish with a reel, headshots, a network and the habits of a professional.</p>

  <div class="photo" style="left:226px;top:12px;width:56px;height:62px" role="img" aria-label="Portrait of alumni actor"></div>
  <div class="quote-name" style="left:226px;top:80px">Dane Holloway</div>
  <p class="copy" style="left:290px;top:12px;width:112px">"The Stage Lantern Hall and Players' Spark Week gave me the tools to walk into any room prepared. I owe a big part of my career to this place and its teachers."</p>
  <p class="copy" style="left:226px;top:100px;width:176px">Starring as Walt Kessler on Night Shift, with film and stage credits across the country.</p>
  <p class="copy" style="left:226px;top:130px;width:176px">Using the proven method of our founders, our core courses turn raw energy into skill. Bring your dream and your drive; we bring the stage, the coaching and the community to help you grow fast.</p>

  <div class="contact">
    <div class="brand" style="position:relative;justify-content:center"><span class="brand__dot"></span>The Stage<br>Lantern Hall</div>
    <div class="contact__addr">2140 Larkmont Avenue<br>Valley Glen, CA 91401</div>
    <div class="contact__phone">818.555.0142</div>
    <div class="contact__web">info@thestagelanternhall.com<br>www.thestagelanternhall.com</div>
  </div>

  <div class="brand" style="left:450px;top:40px;font-size:17px"><span class="brand__dot" style="width:16px;height:16px"></span>The Stage<br>Lantern Hall</div>
  <div class="cover-title">Players'<br>Spark Week</div>
  <div class="photo" style="left:440px;top:180px;width:168px;height:150px;border-radius:10px;background:linear-gradient(160deg,#2a0f0c,#7a3a20 50%,#d59a55)" role="img" aria-label="Theatre auditorium with stage lights"></div>
  <div class="photo photo--round" style="left:470px;top:312px;width:72px;height:72px" role="img" aria-label="Students performing on stage"></div>
  <div class="photo photo--round" style="left:540px;top:300px;width:56px;height:56px" role="img" aria-label="Actor in rehearsal"></div>

  <div class="tagline tagline--red">"IF NOT NOW, WHEN?"</div>
</section>

<section class="spread spread--inside" aria-label="Brochure inside">
  <svg class="layer" width="620" height="479" viewBox="0 0 620 479" aria-hidden="true">
    <path d="M0 360 C160 330 380 400 620 340 L620 479 L0 479 Z" fill="var(--crimson)"/>
  </svg>
  <div class="abs" style="left:0;top:318px;width:620px;height:40px;background:var(--crimson-deep);opacity:.55" role="img" aria-label="City skyline silhouette"></div>

  <div class="fold" style="left:206px"></div>
  <div class="fold" style="left:413px"></div>

  <div class="gold-box" style="left:0;top:14px;width:150px;height:70px"><span>What</span><span class="small">We Believe</span></div>
  <p class="copy" style="left:14px;top:96px;width:120px;color:var(--gold)">The Stage Lantern Hall is simple: we are here to grow actors. Talent is a start, training makes it last, and a community keeps it going.</p>
  <div class="photo" style="left:142px;top:96px;width:50px;height:58px" role="img" aria-label="Portrait of school director"></div>
  <p class="copy copy--dark" style="left:14px;top:160px;width:180px">You need more than raw ability. Working actors know the business as well as the craft, and we teach both from day one, side by side.</p>
  <p class="copy copy--dark" style="left:14px;top:200px;width:180px">Because the best training is done by people who do it, our teachers are active professionals. They share what works right now, not what worked years ago.</p>
  <div class="sign-name" style="left:14px;top:250px">Harold Vance<br>Founder and Artistic Director</div>

  <div class="section-head" style="left:220px;top:16px">Players' Spark Week I<em>(4 weeks)</em></div>
  <p class="copy copy--dark" style="left:220px;top:40px;width:182px">A short, intense start. Four weeks of daily classes in scene work, voice, movement and audition technique. You leave with tools you can use the next morning.</p>
  <div class="gold-box" style="left:300px;top:86px;width:120px;height:64px;padding:7px 8px"><span class="small">What</span><span class="small">We Do About It</span></div>
  <div class="section-head" style="left:220px;top:160px">Players' Spark Week II<em>(8 weeks)</em></div>
  <p class="copy copy--dark" style="left:220px;top:184px;width:182px">The second stage pushes deeper. Longer scenes, on-camera work and showcase prep build the confidence to book the room and hold it.</p>

  <div class="badge" style="left:520px;top:16px"><span class="badge__sq"></span>Spark<br>Week II</div>
  <div class="section-head" style="left:428px;top:60px">The Rising Talent Bundle<em>(3 months)</em></div>
  <p class="copy copy--dark" style="left:428px;top:84px;width:180px">Everything you need to look for work: headshots, a demo reel, résumé polish, agent prep and mock auditions, all in one package. Stop waiting for a break and start making your own.</p>

  <div class="photo photo--round" style="left:10px;top:300px;width:82px;height:82px" role="img" aria-label="Hands raised from a cheering crowd"></div>
  <div class="photo photo--round" style="left:80px;top:350px;width:60px;height:60px" role="img" aria-label="Performer under stage light"></div>
  <div class="photo" style="left:150px;top:270px;width:460px;height:130px;border-radius:8px;background:linear-gradient(120deg,#6b3a2a,#c9946a 45%,#7a4433)" role="img" aria-label="Group of smiling acting students"></div>

  <div class="tagline tagline--white">IF NOT NOW, WHEN?</div>
</section>

</body>
</html>
```